Skincare,Bodycare and haircare brochure

Please design a A4 3 fold brochure for Vexmira Pty Ltd. You may go to our website www.vexmira.example to understand what we do - certified organic skincare.
Content:

About Us: Our Mission
Vexmira’s mission is to make premium skin care products using only certified organic ingredients for a safer, purer world.

How are we diferent?
Vexmira specialises in the research and development of certified organic skin, hair and personal care products for everyone. We hold Certified Organic Licenses with the Verdant Tally Board who accredits our system with the Federal Harvest Purity Code of Australia and other international organic certification standards. Vexmira’s passion is to produce and deliver premium, safe and effective certified organic products to all of our customers.

Other headings: Skincare, Body Care, Hair Care, Essential Oils (leave room for us to put product pictures and product info (you can copy 3 products from each category from our website for draft),

Please provide a heading about our memberships: Please also see our website for info.

Then have a contact us section (doesn't have to be a page) It can even be on the front page.

Please also use the Attached logos. Please use vexmira logo with underline (company logo) and dunbrook crafted and Certified Organic logos.

Many deaigns dont allow me to put alotnof product infronation on it. please allow me to donsoMan

```html
<!DOCTYPE html>
<html lang="en">
<head>
<meta charset="utf-8">
<title>Vexmira Tri-fold Brochure</title>
<link rel="stylesheet" href="https://fonts.googleapis.com/css2?family=Open+Sans:wght@400;600;700;800&family=Oswald:wght@600&display=swap">
<style>
:root{
  --brown:#6e4c31;
  --brown-deep:#4d3322;
  --blush:#dcc8bd;
  --bar-light:#ece2da;
  --ink:#3a281d;
  --label:#3b3b3b;
  --white:#ffffff;
  --green-bottle:#1f2a22;
  --amber:#8a4a22;
}
*{box-sizing:border-box;margin:0;padding:0}
html,body{width:857px;height:1200px;overflow:hidden;background:var(--white)}
body{position:relative;font-family:"Open Sans",Arial,sans-serif;color:var(--ink)}
.panel-label{position:absolute;font-size:19px;color:var(--label);text-align:center;width:250px;transform:translateX(-50%);letter-spacing:.5px}
.panel-label.top{top:14px}
.panel-label.bottom{top:1156px;font-size:20px}

.spread{position:absolute;left:60px;width:747px}
.spread.outside{top:51px;height:538px}
.spread.inside{top:605px;height:533px;background:var(--blush)}
.panel{position:absolute;top:0;height:100%;overflow:hidden}

.product-row::after{content:"";display:block;clear:both}
.product-text{font-size:8.4px;line-height:1.3}
.product-text p{margin-bottom:5px;text-align:justify}
.product-text b{font-weight:700}
.bottle{float:right;margin:0 0 4px 8px;border-radius:4px}
.bottle.oil-bottle{width:42px;height:66px;background:linear-gradient(180deg,#111 0 22%,#e9e4dc 22% 28%,var(--green-bottle) 28% 100%);border:2px solid #e9e4dc}
.bottle.pump{width:36px;height:84px;border-radius:10px 10px 6px 6px;background:linear-gradient(180deg,#1a1a1a 0 24%,var(--amber) 24% 45%,#e7d6b8 45% 70%,var(--amber) 70% 100%)}
.bottle.jar{width:38px;height:46px;background:linear-gradient(180deg,#1c1c1c 0 26%,#234 26% 100%);border-radius:6px}

/* outside flap */
.flap{left:0;width:245px;background:var(--brown);color:var(--white);padding:14px 14px 0 18px}
.flap-title{font-size:12.5px;font-weight:700;letter-spacing:.2px}
.flap-sub{font-size:8px;margin-top:3px;margin-bottom:6px}
.oil{margin-bottom:8px}
.bar-light{background:var(--bar-light);color:var(--ink);font-weight:700;font-size:11.5px;padding:3px 8px;margin:0 0 6px -6px;width:232px;border-radius:0 10px 10px 0;line-height:1.2}

/* back */
.back{left:245px;width:251px;background:var(--blush);padding:16px 14px 0 14px}
.back h2{font-size:13.5px;font-weight:700;color:var(--ink);margin-bottom:6px}
.back p{font-size:8.6px;line-height:1.35;text-align:justify;margin-bottom:12px}
.badges{display:flex;gap:14px;justify-content:center;margin:18px 0 20px}
.badge-round{width:52px;height:52px;border-radius:50%;background:var(--white);border:4px solid #2e6fb0}
.badge-square{width:56px;height:56px;border-radius:6px;background:#2f7a3c;border:3px solid #f1c22c}
.brand{display:flex;flex-direction:column;align-items:center;gap:6px;color:var(--brown-deep)}
.brand-dot{width:26px;height:26px;border-radius:50%;background:var(--brown)}
.brand-name{font-size:22px;font-weight:600;letter-spacing:1.5px}
.back-contact{text-align:center;font-size:8.6px;line-height:1.35;margin-top:10px}
.back-contact .address{margin-bottom:7px}
.contact-line{font-family:"Oswald",Arial,sans-serif;font-size:19px;font-weight:600;text-align:center;margin-top:12px;color:var(--ink)}
.back-url{text-align:center;font-size:10.5px;font-weight:700;letter-spacing:1px;margin-top:2px}

/* front */
.front{left:496px;width:251px;background:var(--brown-deep)}
.front-photo{position:absolute;left:0;top:0;width:251px;height:380px;background:linear-gradient(160deg,#7b5d48 0%,#b79c86 14%,#efe8e0 30%,#e2c2a6 55%,#c99878 75%,#6d8b3d 100%)}
.front-headline{position:absolute;right:12px;top:14px;width:170px;color:var(--white);font-weight:700;font-size:13px;line-height:1.2}
.front-wave{position:absolute;left:0;top:340px;width:251px;height:198px}
.front-brand{position:absolute;left:0;top:432px;width:251px;color:var(--white)}
.front-brand .brand-dot{background:var(--white)}
.front-brand .brand-name{font-size:26px}
.front-url{position:absolute;left:0;width:251px;top:494px;text-align:center;color:var(--white);font-size:11px;letter-spacing:2px;font-weight:600}

/* inside */
.inside .product-text{font-size:7.3px;line-height:1.22}
.inside .product-text p{margin-bottom:4px}
.section-title{font-size:14.5px;font-weight:700;color:var(--ink);letter-spacing:.2px;margin-bottom:2px}
.bar-dark{background:var(--brown);color:var(--white);font-weight:700;font-size:11px;padding:4px 8px;border-radius:0 10px 10px 0;margin:0 0 5px -8px;line-height:1.2}
.product{margin-top:9px}
.inside-left{left:0;width:245px;padding:20px 10px 0 18px}
.inside-left .bar-dark{width:232px}
.massage-photo{position:absolute;left:0;bottom:0;width:245px;height:168px;background:linear-gradient(135deg,#d7b79a 0%,#a9744f 45%,#5a3420 100%);clip-path:path("M0 30 Q120 0 245 20 L245 168 L0 168 Z")}
.inside-center{left:245px;width:251px;padding:22px 10px 0 8px}
.inside-center .bar-dark{width:241px;margin-left:-2px}
.inside-right{left:496px;width:251px}
.hair-photo{position:absolute;right:0;top:0;width:251px;height:196px;background:linear-gradient(100deg,var(--blush) 0%,#b08a6b 28%,#6b3f24 55%,#2a1a10 100%)}
.right-products{position:absolute;left:12px;top:204px;width:229px}
.right-products .bar-dark{width:190px;margin-left:-2px}
.right-products .product:first-child{margin-top:0}
</style>
</head>
<body>

<div class="panel-label top" style="left:183px">OUTSIDE FLAP</div>
<div class="panel-label top" style="left:426px">BACK</div>
<div class="panel-label top" style="left:676px">FRONT</div>

<section class="spread outside">
  <div class="panel flap">
    <div class="flap-title">ESSENTIAL OILS PRODUCTS</div>
    <div class="flap-sub">Certified Organic Oils</div>

    <div class="oil">
      <div class="bar-light">Clementine</div>
      <div class="product-row">
        <div class="bottle oil-bottle" role="img" aria-label="Clementine essential oil bottle"></div>
        <div class="product-text">
          <p><b>Common uses:</b> Clementine essential oil has been known to be helpful for anxiety, nervous tension and restlessness.</p>
          <p><b>Caution:</b> Clementine essential oil is phototoxic. Avoid direct sunlight after applying the oil. Avoid during pregnancy.</p>
        </div>
      </div>
    </div>

    <div class="oil">
      <div class="bar-light">Certified Organic Lemon Essential Oil</div>
      <div class="product-row">
        <div class="bottle oil-bottle" role="img" aria-label="Lemon essential oil bottle"></div>
        <div class="product-text">
          <p><b>Ingredients:</b> Certified Organic Citrus Limon Peel Oil. Application to the skin may increase sensitivity to sunlight.</p>
          <p><b>Common uses:</b> In skin care, Lemon essential oil has been known to have astringent properties which can counter act overproduction of sebum.</p>
          <p><b>Caution:</b> Non-toxic, but may cause skin irritation in some. Lemon is also phototoxic and should be avoided prior to exposure to direct sunlight. Avoid during pregnancy.</p>
        </div>
      </div>
    </div>

    <div class="oil">
      <div class="bar-light">Certified Organic Tea Tree Lemon Scented Oil</div>
      <div class="product-row">
        <div class="bottle oil-bottle" role="img" aria-label="Tea tree lemon scented oil bottle"></div>
        <div class="product-text">
          <p><b>Ingredients:</b> Certified Organic Leptospermum Petersonii Branch/Leaf Oil</p>
          <p><b>Common uses:</b> Lemon Scented Tea Tree has traditionally been used for its anti-viral, anti-inflammatory and anti-septic properties.</p>
          <p><b>Caution:</b> Non-toxic, non-irritant and possibly sensitising to some individuals. Avoid during pregnancy.</p>
        </div>
      </div>
    </div>
  </div>

  <div class="panel back">
    <h2>Our Mission</h2>
    <p>Vexmira’s mission is to make premium skin care products using only certified organic ingredients for a safer, purer world.</p>
    <h2>How are we diferent?</h2>
    <p>Vexmira specialises in the research and development of certified organic skin, hair and personal care products for everyone. We hold Certified Organic Licenses with the Verdant Tally Board who accredits our system with the Federal Harvest Purity Code of Australia and other international organic certification standards. Vexmira’s passion is to produce and deliver premium, safe and effective certified organic products to all of our customers.</p>
    <div class="badges">
      <div class="badge-round" role="img" aria-label="Certified organic membership badge"></div>
      <div class="badge-square" role="img" aria-label="Dunbrook crafted membership badge"></div>
    </div>
    <div class="brand">
      <span class="brand-dot"></span>
      <span class="brand-name">Vexmira</span>
    </div>
    <div class="back-contact">
      <div class="address">Level 4, 22 Quillon Lane, Brisbane,<br>Queensland 4109, Australia. Tel: 07 5550 2846</div>
      <div><b>General:</b> enquiry@vexmira.example</div>
      <div><b>Order:</b> order@vexmira.example</div>
    </div>
    <div class="contact-line">CONTACT US: 07 5550 2846</div>
    <div class="back-url">WWW.VEXMIRA.EXAMPLE</div>
  </div>

  <div class="panel front">
    <div class="front-photo" role="img" aria-label="Spa guest wrapped in a white towel beside green leaves"></div>
    <div class="front-headline">An Exhaustive Resource Of Spa And Massage Treatments</div>
    <svg class="front-wave" viewBox="0 0 251 198" aria-hidden="true">
      <path d="M0 40 Q120 0 251 10 L251 198 L0 198 Z" fill="#5a3c27"/>
      <path d="M0 40 Q120 0 251 10" fill="none" stroke="#e9dcd2" stroke-width="4"/>
    </svg>
    <div class="front-brand brand">
      <span class="brand-dot"></span>
      <span class="brand-name">Vexmira</span>
    </div>
    <div class="front-url">WWW.VEXMIRA.EXAMPLE</div>
  </div>
</section>

<section class="spread inside">
  <div class="panel inside-left">
    <div class="section-title">SKIN CARE PRODUCTS</div>
    <div class="product">
      <div class="bar-dark">Australian Native Facial Cleansing Gel</div>
      <div class="product-row">
        <div class="bottle jar" role="img" aria-label="Facial cleansing gel bottle"></div>
        <div class="product-text">
          <p><b>Ingredients:</b> Purified Water; Vegetable Glycerine; PEG-120 Methyl Glucose Dioleate; Cocoamidopropyl Betaine; Caprylic / Capric Glucoside; Sodium Lauroamphoacetate; Phenoxyethanol; Lavender Australian Oil; Natural Vitamin E; Jojoba Australian Oil; Avocado Oil; Sandalwood Australian Oil; Agonis Fragrans Oil; Cajeput Oil; Extracts from: Kakadu Plum, Lilly Pilly &amp; Quandong; Citric Acid</p>
          <p><b>Directions for use:</b> Apply a small amount of gel to damp skin on the entire face avoiding the eye area. Massage in circular motions and rinse with tepid water or a damp soft cloth. Repeat twice for a double cleanse to remove makeup.</p>
        </div>
      </div>
    </div>
    <div class="product">
      <div class="bar-dark">Certified Organic Moisturising Cream</div>
      <div class="product-row">
        <div class="bottle jar" role="img" aria-label="Moisturising cream jar"></div>
        <div class="product-text">
          <p>These high quality natural ingredients work to help to protect and regenerate the skin. Wrinkles and dark spots are reduced, reversing the signs of aging by deep hydration. Skin will look and feel softer, smoother and more supple for a more youthful complexion. This product will help reverse dry/flaking skin and has healing and antiseptic properties to help with sensitivity.</p>
        </div>
      </div>
    </div>
    <div class="massage-photo" role="img" aria-label="Relaxed guest receiving a spa massage"></div>
  </div>

  <div class="panel inside-center">
    <div class="section-title">BODY CARE PRODUCTS</div>
    <div class="product">
      <div class="bar-dark">Certified Organic Shower and Bath Gel</div>
      <div class="product-row">
        <div class="bottle pump" role="img" aria-label="Shower and bath gel pump bottle"></div>
        <div class="product-text">
          <p>A soothing, moisturising, and beautifully scented shower gel that will cleanse the skin without irritation. The rich moss is full of nutrients for your skin keeping it healthy and youthful.</p>
          <p>Certified Organic Aloe Barbadensis Leaf Juice, Water, Alkyl (C8 to C10) Glucoside, Glycerin, Panthenol, Xanthan Gum, Chondrus Crispus Powder, Potassium Sorbate, Lactic Acid, Citrus Paradisi Peel Oil, Certified Organic Rosa Eglanteria Seed Oil.</p>
        </div>
      </div>
    </div>
    <div class="product">
      <div class="bar-dark">Certified Organic Body Custard</div>
      <div class="product-row">
        <div class="bottle pump" role="img" aria-label="Body custard pump bottle"></div>
        <div class="product-text">
          <p>Our Body Custard is an exclusive range of premium products that have been specially formulated using certified organic ingredients.</p>
          <p>Certified Organic Aloe Barbadensis Leaf Juice, Cetearyl Olivate, Certified Organic Butyrospermum Parkii Butter, Sorbitan Olivate, Glycerin, Certified Organic Simmondsia Chinensis Seed Oil, Certified Organic Cocos Nucifera Oil, Cetearyl Alcohol, Water, Natural Tocopherol, Certified Organic Rosa Eglanteria Seed Oil, Certified Organic Prunus Amygdalus Dulcis Oil, Cedrus Atlantica Bark Oil, Certified Organic Zingiber Officinale Root Oil</p>
        </div>
      </div>
    </div>
    <div class="product">
      <div class="bar-dark">Certified Organic Body Lotion</div>
      <div class="product-row">
        <div class="bottle pump" role="img" aria-label="Body lotion pump bottle"></div>
        <div class="product-text">
          <p>Certified Organic Aloe Barbadensis Leaf Juice, Glycerin, Cetearyl Olivate, Sorbitan Olivate, Certified Organic Butyrospermum Parkii Butter, Cetearyl Alcohol, Water, Natural Tocopherol, Certified Organic Simmondsia Chinensis Seed Oil, Certified Organic Prunus Amygdalus Dulcis Oil, Certified Organic Persea Gratissima Oil, Certified Organic Macadamia Integrifolia Seed Oil, Potassium Sorbate, Certified Organic Citrus Reticulata Peel Oil, Lactic Acid, Certified Organic Litsea Cubeba Oil, Cedrus Atlantica Bark Oil</p>
        </div>
      </div>
    </div>
  </div>

  <div class="panel inside-right">
    <div class="hair-photo" role="img" aria-label="Long flowing healthy hair"></div>
    <div class="right-products">
      <div class="product">
        <div class="bar-dark">Certified Organic Shampoo</div>
        <div class="product-row">
          <div class="bottle pump" role="img" aria-label="Shampoo pump bottle"></div>
          <div class="product-text">
            <p>Certified Organic Aloe Barbadensis Leaf Juice, Cetearyl Olivate, Glycerin, Sorbitan Olivate, Certified Organic Butyrospermum Parkii Butter, Cetearyl Alcohol, Water, Natural Tocopherol, Panthenol, Certified Organic Rosa Eglanteria Seed Oil, Certified Organic Persea Gratissima Oil, Certified Organic Simmondsia Chinensis Seed Oil, Potassium Sorbate, Lactic Acid, Citrus Paradisi Peel Oil, Certified Organic Backhousia Citriodora Oil, Certified Organic Litsea Cubeba Fruit Oil</p>
          </div>
        </div>
      </div>
      <div class="product">
        <div class="bar-dark">Certified Organic Conditioner</div>
        <div class="product-row">
          <div class="bottle pump" role="img" aria-label="Conditioner pump bottle"></div>
          <div class="product-text">
            <p>Our Made with Organic Conditioner is an exclusive range of premium products that have been specially formulated using certified organic ingredients.</p>
            <p>Certified Organic Aloe Barbadensis Leaf Juice, Cetearyl Olivate, Glycerin, Sorbitan Olivate, Certified Organic Butyrospermum Parkii Butter, Cetearyl Alcohol, Water, Natural Tocopherol, Panthenol, Certified Organic Rosa Eglanteria Seed Oil, Certified Organic Persea Gratissima Oil, Certified Organic Simmondsia Chinensis Seed Oil, Potassium Sorbate, Lactic Acid.</p>
          </div>
        </div>
      </div>
    </div>
  </div>
</section>

<div class="panel-label bottom" style="left:181px">Inside Left</div>
<div class="panel-label bottom" style="left:430px">Inside Center</div>
<div class="panel-label bottom" style="left:681px">Inside Right</div>

</body>
</html>
```